Flyer for Medical practice welcoming new patients

We need a DL size brochure designed for Medical practice to advertise that we are accepting new patients. Our practice has special interests in women's and children's health and seniors health. Our existing advertising materials are in the colour scheme of purples I have uploaded our logo which includes our colour scheme.

Target Market(s)

Versatile to target anyone looking for a small medical practice that offers continuous care of seeing the same Doctor every time

Industry/Entity Type

Advertising

Font styles to use
Serif

Colors
6b449b
876aae
b7a5cc

Requirements
Must have
• The practice logo of just the picture not Dr Wanda Thorpe.
• Purple colour scheme.
• Practice name: Bramblecote Medical Practice.
• Address: 147 Tolley Rd, Bramblecote NSW 2500.
• Phone: 4371 5806.
• DL size brochure
• Welcoming new patients ( a strong emphasis needs to be placed on this)
• Nurse and onsite ECG's and lung function tests.
• Travel vaccines including yellow fever
• Bulk billing for tertiary students
• We would also like design to alter the text so that we can change the points to be reflect who we are targeting at the time.
Nice to have
• The practice logo with Dr Wanda Thorpe somewhere not as a feature as the practice no longer goes under this name but is still well known as Dr Thorpe's.

```html
<!DOCTYPE html>
<html lang="en">
<head>
<meta charset="utf-8">
<title>Bramblecote Medical Practice – accepting new patients</title>
<link rel="stylesheet" href="https://fonts.googleapis.com/css2?family=Crimson+Text:wght@400;700&family=Sorts+Mill+Goudy&display=swap">
<style>
  :root {
    --purple-deep: #6b449b;
    --purple-mid: #876aae;
    --purple-light: #b7a5cc;
    --lavender: #e6ddef;
    --lavender-pale: #f3eff8;
    --white: #ffffff;
  }
  * { box-sizing: border-box; margin: 0; padding: 0; }
  html, body { width: 1200px; height: 600px; overflow: hidden; background: var(--white); }
  .flyer {
    position: relative;
    width: 1200px;
    height: 600px;
    overflow: hidden;
    background: var(--white);
    font-family: "Crimson Text", Georgia, serif;
    color: var(--purple-deep);
  }
  .flyer > * { position: absolute; }

  .top-ribbon { left: 0; top: 0; width: 1200px; height: 140px; }
  .corner-ornament {
    left: 0; top: 0; width: 100px; height: 80px;
    background: radial-gradient(circle at 40% 40%, var(--lavender) 0%, var(--lavender-pale) 70%, transparent 100%);
  }

  .feature-photo {
    left: 830px; top: 130px; width: 370px; height: 390px;
    background: linear-gradient(90deg, rgba(255,255,255,1) 0%, rgba(230,221,239,0.7) 25%, var(--lavender) 55%, var(--purple-light) 100%);
  }

  .practice-name {
    left: 48px; top: 102px;
    font-family: "Sorts Mill Goudy", Georgia, serif;
    font-weight: 400;
    font-size: 80px;
    line-height: 1;
    color: var(--purple-deep);
    white-space: nowrap;
    transform: rotate(-3.4deg);
    transform-origin: 0 100%;
  }

  .grid-rule { background: var(--purple-light); }
  .grid-rule--horizontal { left: 40px; top: 356px; width: 820px; height: 2px; }
  .grid-rule--vertical { left: 324px; top: 200px; width: 2px; height: 320px; }

  .stripe-block {
    background: linear-gradient(90deg, var(--purple-light), var(--lavender-pale));
    opacity: 0.8;
  }
  .stripe-block--one { left: 200px; top: 220px; width: 110px; height: 110px; }
  .stripe-block--two { left: 466px; top: 220px; width: 104px; height: 110px; }
  .stripe-block--three { left: 350px; top: 380px; width: 110px; height: 120px;
    background: linear-gradient(180deg, var(--purple-light), var(--lavender-pale)); }

  .service {
    font-size: 30px;
    line-height: 32px;
    color: var(--purple-deep);
  }
  .service strong { font-weight: 700; display: block; }
  .service span { display: block; }

  .service--accepting { left: 332px; top: 222px; width: 130px; text-align: center; }
  .service--billing { left: 580px; top: 196px; }
  .service--travel { left: 60px; top: 362px; width: 256px; text-align: right; }
  .service--testing { left: 474px; top: 362px; }

  .doctor-mark {
    left: 576px; top: 462px;
    display: flex; align-items: center; gap: 14px;
  }
  .doctor-mark__dot {
    width: 40px; height: 40px; border-radius: 50%;
    background: var(--purple-light);
  }
  .doctor-mark__name {
    font-size: 40px; font-weight: 400; line-height: 1;
    color: var(--purple-deep);
    white-space: nowrap;
  }

  .contact-band { left: 0; top: 520px; width: 1200px; height: 80px; }
  .contact-band__accent { position: absolute; left: 0; top: 0; width: 100%; height: 10px; background: var(--purple-mid); }
  .contact-band__bar { position: absolute; left: 0; top: 10px; width: 100%; height: 70px; background: var(--purple-deep); }
  .contact-line {
    position: absolute; right: 40px; top: 28px;
    font-size: 26px; font-weight: 700; line-height: 34px;
    color: var(--white); white-space: nowrap;
  }
</style>
</head>
<body>
<main class="flyer">
  <svg class="top-ribbon" viewBox="0 0 1200 140" aria-hidden="true">
    <polygon points="0,100 1200,6 1200,40 0,130" fill="#f3eff8"/>
    <polygon points="90,96 1200,18 1200,30 90,108" fill="#e6ddef"/>
    <line x1="90" y1="96" x2="1200" y2="18" stroke="#b7a5cc" stroke-width="2"/>
  </svg>
  <div class="corner-ornament" role="img" aria-label="Soft swirl ornament"></div>

  <div class="feature-photo" role="img" aria-label="Photo of a hand holding an ECG printout, tinted purple"></div>

  <h1 class="practice-name">Bramblecote Medical Practice</h1>

  <div class="grid-rule grid-rule--horizontal"></div>
  <div class="grid-rule grid-rule--vertical"></div>

  <div class="stripe-block stripe-block--one" role="img" aria-label="Striped accent block"></div>
  <div class="stripe-block stripe-block--two" role="img" aria-label="Striped accent block"></div>
  <div class="stripe-block stripe-block--three" role="img" aria-label="Striped accent block"></div>

  <p class="service service--accepting"><strong>accepting</strong><span>new</span><span>patients</span></p>
  <p class="service service--billing"><strong>bulk billing</strong><span>for tertiary</span><span>students</span></p>
  <p class="service service--travel"><strong>travel vaccines</strong><span>including</span><span>yellow fever</span></p>
  <p class="service service--testing"><strong>onsite ECG's</strong><span>and lung</span><span>function tests</span></p>

  <div class="doctor-mark">
    <span class="doctor-mark__dot"></span>
    <span class="doctor-mark__name">Dr Wanda Thorpe</span>
  </div>

  <footer class="contact-band">
    <div class="contact-band__accent"></div>
    <div class="contact-band__bar"></div>
    <p class="contact-line">147 Tolley Rd, Bramblecote NSW 2500 | &nbsp;phone 4371 5806.</p>
  </footer>
</main>
</body>
</html>
```